Consulting company needs Business Cards - rough concept provided

I'm looking for someone to take our business card idea and make is slick and polished - to communicate our high-end, sophisticated, serious consulting business. We have a rough layout we did in-house. We are open to ideas on repo-ing elements, adjusting sizes, typefaces etc... within the general concept we've already come up with. We want it to be super-clean and sophisticated. We want to keep the white backgrounds, and blue brand colors. Our goal is to print with painted blue edges on thick cardstock. Thank you!!

```html
<!DOCTYPE html>
<html lang="en">
<head>
<meta charset="utf-8">
<title>Norvale Business Cards</title>
<link rel="stylesheet" href="https://fonts.googleapis.com/css2?family=Montserrat:wght@300;400;500;700;800&display=swap">
<style>
  :root {
    --page-bg: #edf1f8;
    --card-edge: #bdbec0;
    --card-white: #ffffff;
    --brand-blue: #009bdb;
    --ink: #111111;
    --muted: #a9abae;
    --label: #111111;
  }
  * { box-sizing: border-box; margin: 0; padding: 0; }
  html, body { width: 1200px; height: 1000px; overflow: hidden; }
  body {
    background: var(--page-bg);
    font-family: "Montserrat", sans-serif;
    position: relative;
  }
  .version-label {
    position: absolute;
    top: 98px;
    width: 200px;
    text-align: center;
    font-weight: 300;
    font-size: 48px;
    color: var(--label);
    letter-spacing: 2px;
  }
  .version-label--one { left: 189px; }
  .version-label--two { left: 807px; }

  .card {
    position: absolute;
    width: 493px;
    height: 286px;
    border: 9px solid var(--card-edge);
    background: var(--card-white);
    box-shadow: 0 6px 14px rgba(0,0,0,0.12);
    overflow: hidden;
  }
  .card--front-one { left: 55px; top: 174px; }
  .card--front-two { left: 651px; top: 174px; }
  .card--back { left: 354px; top: 606px; }

  .blue-panel {
    position: absolute;
    left: 165px; top: 0; right: 0; bottom: 0;
    background: var(--brand-blue);
  }
  .accent-bar {
    position: absolute;
    width: 84px; height: 12px;
    background: var(--brand-blue);
  }
  .accent-bar--bottom-left { left: 0; bottom: 0; }
  .accent-bar--top-left { left: 0; top: 0; }
  .accent-bar--top-right { right: 0; top: 0; }

  .person {
    position: absolute;
    line-height: 1;
  }
  .person--top { left: 14px; top: 14px; }
  .person--bottom { left: 20px; top: 213px; }
  .person__first {
    display: block;
    font-size: 17px;
    font-weight: 400;
    color: var(--ink);
  }
  .person__last {
    display: block;
    font-size: 17px;
    font-weight: 800;
    color: var(--ink);
    margin-top: -1px;
  }
  .person__title {
    display: block;
    font-size: 8.5px;
    font-weight: 400;
    color: var(--brand-blue);
    margin-top: 2px;
  }

  .brand-name {
    position: absolute;
    left: 165px; right: 0;
    top: 100px;
    text-align: center;
    font-size: 56px;
    font-weight: 800;
    color: var(--card-white);
    letter-spacing: 1px;
    line-height: 1;
  }

  .contact {
    position: absolute;
    left: 329px; top: 193px;
    padding-left: 7px;
    border-left: 3px solid var(--card-edge);
    color: var(--card-white);
    font-size: 10px;
    font-weight: 400;
    line-height: 12.5px;
  }
  .contact__line--gap { margin-top: 4px; }

  .promise {
    position: absolute;
    left: 26px; top: 46px;
    font-size: 20px;
    line-height: 47px;
    letter-spacing: 1.6px;
    font-weight: 300;
    color: var(--muted);
  }
  .promise strong {
    font-weight: 800;
    color: var(--brand-blue);
    letter-spacing: 1px;
  }
</style>
</head>
<body>
  <div class="version-label version-label--one">V1</div>
  <div class="version-label version-label--two">V2</div>

  <section class="card card--front-one">
    <div class="blue-panel"></div>
    <div class="accent-bar accent-bar--bottom-left"></div>
    <div class="person person--top">
      <span class="person__first">DANA</span>
      <span class="person__last">WHITLOCK</span>
      <span class="person__title">BRAND CONSULTANT</span>
    </div>
    <div class="brand-name">NORVALE</div>
    <div class="contact">
      <div>4820 Harbor Lane,Ste 210</div>
      <div>Millbrook, Ca 90417</div>
      <div class="contact__line--gap">555 014 2290</div>
      <div class="contact__line--gap">dana@norvale.com</div>
    </div>
  </section>

  <section class="card card--front-two">
    <div class="blue-panel"></div>
    <div class="accent-bar accent-bar--top-left"></div>
    <div class="person person--bottom">
      <span class="person__first">DANA</span>
      <span class="person__last">WHITLOCK</span>
      <span class="person__title">BRAND CONSULTANT</span>
    </div>
    <div class="brand-name">NORVALE</div>
    <div class="contact">
      <div>4820 Harbor Lane,Ste 210</div>
      <div>Millbrook, Ca 90417</div>
      <div class="contact__line--gap">555 014 2290</div>
      <div class="contact__line--gap">dana@norvale.com</div>
    </div>
  </section>

  <section class="card card--back">
    <div class="accent-bar accent-bar--top-right"></div>
    <div class="accent-bar accent-bar--bottom-left"></div>
    <p class="promise">
      <strong>we help</strong> [target demographic] <strong>achieve</strong><br>
      [desired emotional outcome] <strong>by</strong> [our<br>
      unique approach] <strong>because</strong> [our brand<br>
      beliefs]
    </p>
  </section>
</body>
</html>
```